Executive Coaching and Spiritual Development Company needs a business card design.

We need a business card design for our company. We already have a logo that was created through Inkharbor that we will submit and would like to see this work on black, blue and white backgrounds. Our personal information should be included as well. The design should communicate trust, spirituality, support and partnership.

Industry/Entity Type

Business

Colors
0255a3
33a6d7
ffffff
000000
474747

Requirements
Nice to have
• The colors offered here are just ideas--we are open to other suggestions, too.

```html
<!DOCTYPE html>
<html lang="en">
<head>
<meta charset="utf-8">
<title>Stillwater Business Card</title>
<link href="https://fonts.googleapis.com/css2?family=Arvo:wght@400&family=Source+Sans+3:wght@300;400&display=swap" rel="stylesheet">
<style>
  :root {
    --canvas-bg: #e9e7e3;
    --card-dark: #0b1a22;
    --card-light: #ffffff;
    --ink-dark: #0d1b24;
    --ink-body: #2b2f33;
    --ink-muted: #474747;
    --ink-light: #ffffff;
    --shadow: rgba(0, 0, 0, 0.18);
  }
  * { margin: 0; padding: 0; box-sizing: border-box; }
  html, body { width: 1200px; height: 1000px; overflow: hidden; }
  body {
    background: var(--canvas-bg);
    position: relative;
    font-family: "Source Sans 3", "Source Sans Pro", sans-serif;
  }
  .card {
    position: absolute;
    width: 760px;
    height: 434px;
    box-shadow: 0 6px 18px var(--shadow);
    overflow: hidden;
  }
  .card--front { left: 90px; top: 50px; background: var(--card-dark); }
  .card--back  { left: 350px; top: 516px; background: var(--card-light); }

  .brand { position: absolute; display: flex; align-items: center; }
  .brand__mark { border-radius: 50%; flex: none; }
  .brand__name { font-family: "Arvo", serif; font-weight: 400; line-height: 1; }

  .card--front .brand { left: 92px; top: 142px; gap: 26px; }
  .card--front .brand__mark { width: 148px; height: 148px; border: 3px solid var(--ink-light); }
  .card--front .brand__name { color: var(--ink-light); font-size: 92px; }

  .card--back .brand { left: 352px; top: 30px; gap: 16px; }
  .card--back .brand__mark { width: 82px; height: 82px; border: 3px solid var(--ink-dark); }
  .card--back .brand__name { color: var(--ink-dark); font-size: 48px; }

  .decor-ring {
    position: absolute;
    left: -190px;
    top: -20px;
    width: 420px;
    height: 420px;
    border-radius: 50%;
    border: 5px solid var(--ink-dark);
  }

  .person { position: absolute; right: 88px; top: 150px; text-align: right; }
  .person__name {
    font-size: 25px; font-weight: 400; letter-spacing: 1.5px;
    color: var(--ink-dark); text-transform: uppercase;
  }
  .person__title { font-size: 17px; font-weight: 400; color: var(--ink-muted); margin-top: 4px; }

  .contacts {
    position: absolute; right: 40px; top: 246px;
    list-style: none;
  }
  .contacts__item {
    display: flex; justify-content: flex-end; align-items: center;
    gap: 18px; height: 30px;
    font-size: 18px; font-weight: 300; color: var(--ink-body);
  }
  .contacts__icon { width: 20px; height: 20px; flex: none; fill: var(--ink-dark); }
</style>
</head>
<body>

  <section class="card card--front" aria-label="Business card front">
    <div class="brand">
      <span class="brand__mark"></span>
      <span class="brand__name">Stillwater</span>
    </div>
  </section>

  <section class="card card--back" aria-label="Business card back">
    <div class="decor-ring"></div>

    <div class="brand">
      <span class="brand__mark"></span>
      <span class="brand__name">Stillwater</span>
    </div>

    <div class="person">
      <p class="person__name">Mara Ellison</p>
      <p class="person__title">General Manager</p>
    </div>

    <ul class="contacts">
      <li class="contacts__item">+021 555 014 220
        <svg class="contacts__icon" viewBox="0 0 24 24"><path d="M6.6 10.8a15 15 0 0 0 6.6 6.6l2.2-2.2c.3-.3.7-.4 1-.2 1.1.4 2.3.6 3.6.6.6 0 1 .4 1 1V20c0 .6-.4 1-1 1A17 17 0 0 1 3 4c0-.6.4-1 1-1h3.5c.6 0 1 .4 1 1 0 1.3.2 2.5.6 3.6.1.3 0 .7-.2 1z"/></svg>
      </li>
      <li class="contacts__item">+541 555 018 3342
        <svg class="contacts__icon" viewBox="0 0 24 24"><path d="M7 1h10a2 2 0 0 1 2 2v18a2 2 0 0 1-2 2H7a2 2 0 0 1-2-2V3a2 2 0 0 1 2-2zm0 3v15h10V4zm5 16.2a.9.9 0 1 0 0 1.8.9.9 0 0 0 0-1.8z"/></svg>
      </li>
      <li class="contacts__item">+098 555 016 7719
        <svg class="contacts__icon" viewBox="0 0 24 24"><path d="M6 2h12v5H6zM4 8h16a2 2 0 0 1 2 2v7h-4v5H6v-5H2v-7a2 2 0 0 1 2-2zm4 7v5h8v-5zm10-5a1 1 0 1 0 0 2 1 1 0 0 0 0-2z"/></svg>
      </li>
      <li class="contacts__item">mara@stillwaterpath.com
        <svg class="contacts__icon" viewBox="0 0 24 24"><path d="M2 5h20v2l-10 6L2 7zm0 4.3 10 6 10-6V19H2z"/></svg>
      </li>
      <li class="contacts__item">www.stillwaterpath.com
        <svg class="contacts__icon" viewBox="0 0 24 24"><path d="M12 2a10 10 0 1 0 0 20 10 10 0 0 0 0-20zm0 2c.9 0 2.2 1.8 2.8 5H9.2C9.8 5.8 11.1 4 12 4zM4.3 9h2.9a17 17 0 0 0 0 6H4.3a8 8 0 0 1 0-6zm4.9 0h5.6a15 15 0 0 1 0 6H9.2a15 15 0 0 1 0-6zm7.6 0h2.9a8 8 0 0 1 0 6h-2.9a17 17 0 0 0 0-6zM9.2 17h5.6c-.6 3.2-1.9 5-2.8 5s-2.2-1.8-2.8-5z"/></svg>
      </li>
    </ul>
  </section>

</body>
</html>
```